Fact Sheets for Insurance

We need a 4 page booklet brochure designed for our insurance business. Each page is A4. We design insurance plans for our Clients and we wish to use the brochure to market and educate our Client and business partners. The business is Halvard Mensley Financial Services. Colour scheme of our logo and stationary is navy blue and metallic gold. The content has been drafted and each page is attached. Please use your creative freedom to make it look professional and modern. We would like graphics, pictures etc to make it more vibrant as well.

Industry/Entity Type

Insurance

```html
<!DOCTYPE html>
<html lang="en">
<head>
<meta charset="utf-8">
<title>Insurance Cheat Sheets – Halvard Mensley Financial Services</title>
<link href="https://fonts.googleapis.com/css2?family=Libre+Baskerville:wght@400;700&family=Open+Sans:wght@400;600;700;800&display=swap" rel="stylesheet">
<style>
:root{
  --navy:#1c3a6b;
  --navy-deep:#12264a;
  --navy-soft:#3d5f93;
  --gold:#a88e58;
  --gold-light:#c9b27f;
  --tan:#c7b283;
  --paper:#e6eaf0;
  --row:#d3d9e3;
  --ink:#1f2a3d;
  --white:#ffffff;
}
*{margin:0;padding:0;box-sizing:border-box}
html,body{width:1200px;height:414px;overflow:hidden;background:var(--white)}
body{position:relative;font-family:"Open Sans",Arial,sans-serif;color:var(--ink)}
.page{position:absolute;top:0;height:414px;overflow:hidden}
.page--life{left:0;width:291px;background:var(--paper)}
.page--income{left:303px;width:297px;background:var(--tan)}
.page--critical{left:600px;width:295px;background:var(--tan)}
.page--tpd{left:907px;width:293px;background:var(--paper)}
.photo{position:absolute;left:0;width:100%}
.tab{position:absolute;top:6px;height:15px;padding:0 8px;background:var(--navy);color:var(--white);font-weight:700;font-size:10px;line-height:15px;letter-spacing:.2px;display:flex;align-items:center;gap:5px}
.tab::after{content:"";width:8px;height:8px;border-radius:50%;background:var(--white);opacity:.8}
.banner-title{position:absolute;font-family:"Libre Baskerville",Georgia,serif;text-transform:uppercase;line-height:1.15;white-space:nowrap}
.col{position:absolute}
.h-section{font-weight:800;font-size:9.5px;color:var(--navy);text-transform:uppercase;text-align:center;line-height:1.15;letter-spacing:.1px}
.need-table{width:100%;border-collapse:collapse;font-size:6px;margin-top:4px}
.need-table th{background:var(--navy);color:var(--gold-light);font-family:"Libre Baskerville",Georgia,serif;font-weight:700;font-size:6px;padding:2px 3px;text-align:center}
.need-table td{padding:1.6px 3px;color:var(--navy)}
.need-table td:first-child{text-align:right;width:56%}
.need-table tr:nth-child(odd) td{background:var(--row)}
.need-table tr:nth-child(even) td{background:#eef1f5}
.need-table tr.total td{background:var(--navy);color:var(--gold-light);font-family:"Libre Baskerville",Georgia,serif;font-weight:700;text-align:center}
.tips p{font-size:5.6px;line-height:1.36;margin-top:5px;color:var(--ink)}
.tips b{font-weight:700;color:var(--navy)}
.tips .faded{opacity:.55}
.list{list-style:none;margin-top:4px}
.list li{font-size:5.8px;line-height:1.3;padding-left:9px;position:relative;margin-bottom:2px}
.list li::before{content:"";position:absolute;left:1px;top:2.3px;width:3px;height:3px;background:var(--navy)}
.help{font-size:5.8px;margin-top:7px}
.callout{font-weight:800;font-variant:small-caps;color:var(--navy);font-size:8.6px;line-height:1.18;margin-top:10px;letter-spacing:.15px}
.footer-url{position:absolute;bottom:3px;font-size:4.8px;color:var(--white);opacity:.85}
.brand{position:absolute;display:flex;align-items:center;gap:5px;font-family:"Libre Baskerville",Georgia,serif;font-weight:400;color:var(--white);font-size:10px;line-height:1.1}
.brand-mark{width:14px;height:14px;border-radius:50%;background:var(--white)}
.contact{position:absolute;right:10px;bottom:20px;text-align:right;font-size:6px;color:var(--white);line-height:1.5}
.legal{position:absolute;right:10px;bottom:6px;font-size:4.6px;color:var(--white);opacity:.85}
.disclaimer{position:absolute;left:10px;top:355px;width:170px;font-size:4.2px;line-height:1.3;color:var(--white);opacity:.6}
</style>
</head>
<body>

<section class="page page--life">
  <div class="photo" style="top:0;height:118px;background:linear-gradient(120deg,#b98c6b 0%,#d9b28d 35%,#8e6f88 65%,#5b4e71 100%)" role="img" aria-label="Photo of a smiling multi-generation family celebrating together"></div>
  <div class="tab" style="left:0">CHEAT SHEET</div>
  <svg style="position:absolute;left:0;top:78px" width="291" height="40" viewBox="0 0 291 40">
    <path d="M0 6 L291 0 L291 34 L0 40Z" fill="var(--gold)"/>
  </svg>
  <div class="banner-title" style="left:0;width:291px;top:91px;text-align:center;color:var(--white);font-size:12.5px">Buying Life Insurance</div>
  <svg style="position:absolute;left:0;top:300px" width="291" height="114" viewBox="0 0 291 114">
    <path d="M148 114 C190 70 240 40 291 30 L291 114Z" fill="var(--navy-soft)" opacity=".55"/>
    <path d="M150 114 C195 80 245 58 291 50 L291 114Z" fill="var(--navy)"/>
    <path d="M170 114 C210 96 250 86 291 82 L291 114Z" fill="var(--navy-deep)"/>
  </svg>

  <div class="col" style="left:10px;top:121px;width:134px">
    <h2 class="h-section">How much do I need?</h2>
    <table class="need-table">
      <tr><th>NEED</th><th>AMOUNT</th></tr>
      <tr><td>Repaying Debts</td><td>$</td></tr>
      <tr><td>Funeral Expenses</td><td>$</td></tr>
      <tr><td>Replacing your income</td><td>$</td></tr>
      <tr><td>Other</td><td>$</td></tr>
      <tr class="total"><td>TOTAL</td><td>$</td></tr>
    </table>
    <h2 class="h-section" style="margin-top:8px">Tips &amp; Traps</h2>
    <div class="tips">
      <p>Ensure contract <b>covers all causes of death</b>, not just accidents.</p>
      <p><b>Review exclusions.</b> The only standard industry exclusion is “suicide within first 13 months of policy inception or reinstatement”.</p>
      <p>Look to <b>purchase “Long Term” Life Insurance</b> if you think you will need to hold the policy for a number of years. This may save you tens of thousands of dollars over the life of your policy.</p>
      <p>Ensure the contract is <b>guaranteed to be renewed</b> if you pay your premiums until expiry age.</p>
      <p>If purchased through Super, your <b>beneficiaries may be liable for a tax bill</b> in the event of a claim</p>
    </div>
  </div>

  <div class="col" style="left:153px;top:121px;width:130px">
    <h2 class="h-section">Who offers it?</h2>
    <ul class="list">
      <li>Most Superannuation Funds</li>
      <li>Some Private Health Funds</li>
      <li>Some Employers</li>
      <li>Life Insurance Companies</li>
      <li>General Insurance Companies</li>
    </ul>
    <h2 class="h-section" style="margin-top:8px">When to call a professional adviser?</h2>
    <p class="help">If you need help:</p>
    <ul class="list">
      <li>comparing premiums or policies</li>
      <li>reviewing wording of insurance contracts</li>
      <li>structuring your policies to get a tax deduction</li>
      <li>avoiding tax on any claim proceeds</li>
      <li>purchasing “Long Term” Life Insurance</li>
    </ul>
    <p class="callout">If you want to ensure that you have someone assisting your family if a claim is ever needed to be made.</p>
  </div>

  <div class="brand" style="left:178px;top:378px"><span class="brand-mark"></span><span>Halvard Mensley<br><span style="font-size:6px">Financial Services</span></span></div>
</section>

<section class="page page--income">
  <div class="photo" style="top:0;height:112px;background:linear-gradient(135deg,#f4f4f2 0%,#d7dade 60%,#b9bec7 100%)" role="img" aria-label="Photo of a printed household budget list with family income and expenses"></div>
  <div class="tab" style="left:0">CHEAT SHEET</div>
  <svg style="position:absolute;left:0;top:88px" width="297" height="70" viewBox="0 0 297 70">
    <path d="M0 6 C100 0 200 20 297 10 L297 62 L0 62Z" fill="var(--navy)"/>
    <path d="M0 56 C100 48 200 66 297 56 L297 70 L0 70Z" fill="var(--gold)"/>
  </svg>
  <div class="banner-title" style="left:18px;top:108px;color:var(--white);font-size:12px">Buying Income<br>Protection Insurance</div>

  <div class="col" style="left:18px;top:158px;width:135px">
    <h2 class="h-section">How much do I need?</h2>
    <div class="tips"><p style="margin-top:4px">Most people insure 75% of their income, which is the maximum benefit that Insurance Companies generally cover.</p></div>
    <h2 class="h-section" style="margin-top:8px">Tips &amp; Traps</h2>
    <div class="tips">
      <p>Ensure Policy <b>covers all illnesses and injuries</b>, not just accidents.</p>
      <p><b>Review what the policy doesn’t cover “Exclusions”.</b> Standard exclusions include self-inflicted acts, pregnancy related illnesses and war related claims.</p>
      <p><b>Understand the definitions of “Total and Partial Disability”</b> so you know when you can make a claim.</p>
      <p class="faded">Look to <b>purchase “Long Term” Life Insurance</b> if you think you will need to hold the policy for a number of years. This may save you tens of thousands of dollars over the life of your policy.</p>
      <p>Ensure the contract is <b>guaranteed to be renewed</b> if you pay your premiums until expiry age.</p>
      <p class="faded">Paying the premiums yourself, will generally enable you <b>to claim a tax deduction</b></p>
    </div>
  </div>

  <div class="col" style="left:162px;top:158px;width:128px">
    <h2 class="h-section">Who offers it?</h2>
    <ul class="list">
      <li>Most Superannuation Funds</li>
      <li>Some Private Health Funds</li>
      <li>Some Employers</li>
      <li>Life Insurance Companies</li>
      <li>General Insurance Companies</li>
    </ul>
    <h2 class="h-section" style="margin-top:7px">When to call a professional adviser?</h2>
    <p class="help" style="margin-top:5px">If you need help:</p>
    <ul class="list">
      <li>comparing premiums</li>
      <li>reviewing &amp; comparing policy terms and conditions</li>
      <li>matching a policy to suit your occupation</li>
      <li>deciding on the appropriate Waiting Periods and Benefit Periods</li>
      <li>purchasing “Long Term” Life Insurance</li>
    </ul>
    <p class="callout" style="font-size:7.2px;margin-top:6px">If you want to ensure that you have someone assisting you if a claim is ever needed to be made.</p>
    <p class="callout" style="font-size:7.2px;margin-top:5px">If your financial affairs are complex due to being self-employed or a high income earner.</p>
  </div>

  <svg style="position:absolute;left:0;top:398px" width="297" height="16" viewBox="0 0 297 16">
    <path d="M0 6 C100 0 200 10 297 4 L297 16 L0 16Z" fill="var(--navy)"/>
  </svg>
  <div class="footer-url" style="left:14px">www.halvardmensley.com.au</div>
</section>

<section class="page page--critical">
  <div class="photo" style="top:0;height:112px;background:linear-gradient(100deg,#9fb0bf 0%,#c9d3db 40%,#7f97ad 75%,#5e7891 100%)" role="img" aria-label="Photo of hospital staff wheeling a patient trolley down a corridor"></div>
  <div class="tab" style="right:0">CHEAT SHEET</div>
  <svg style="position:absolute;left:0;top:82px" width="295" height="76" viewBox="0 0 295 76">
    <path d="M0 14 L295 4 L295 58 L0 66Z" fill="var(--navy)"/>
    <path d="M0 62 L295 54 L295 76 L0 76Z" fill="var(--gold)"/>
    <rect x="12" y="5" width="283" height="26" fill="#eef1f5"/>
  </svg>
  <div class="banner-title" style="left:20px;top:94px;color:var(--navy);font-size:10.5px;font-weight:700">Buying Critical Illness Insurance</div>

  <div class="col" style="left:14px;top:162px;width:132px">
    <h2 class="h-section">How much do I need?</h2>
    <table class="need-table">
      <tr><th>NEED</th><th>AMOUNT</th></tr>
      <tr><td>Medical Expenses</td><td>$</td></tr>
      <tr><td>Other</td><td>$</td></tr>
      <tr class="total"><td>TOTAL</td><td>$</td></tr>
    </table>
    <h2 class="h-section" style="margin-top:18px">Tips &amp; Traps</h2>
    <div class="tips">
      <p><b>Pay particular attention to the definitions for Cancer and Cardiovascular conditions</b> such as Heart Attack so you are aware of when you can claim.</p>
      <p><b>Review what the policy doesn’t cover “Exclusions”. Standard exclusion</b> for most policies is self-inflicted acts.</p>
      <p>Look to <b>purchase “Long Term” Life Insurance</b> if you think you will need to hold the policy for a number of years. This may save you tens of thousands of dollars over the life of your policy.</p>
      <p>Ensure the contract is <b>guaranteed to be renewed</b> if you pay your premiums until expiry age.</p>
    </div>
  </div>

  <div class="col" style="left:158px;top:162px;width:128px">
    <h2 class="h-section">Who offers it?</h2>
    <ul class="list">
      <li>Some Private Health Funds</li>
      <li>Some Employers</li>
      <li>Life Insurance Companies</li>
      <li>General Insurance Companies</li>
    </ul>
    <h2 class="h-section" style="margin-top:14px">When to call a professional adviser?</h2>
    <p class="help">If you need help:</p>
    <ul class="list">
      <li>comparing premiums or policies</li>
      <li>reviewing &amp; comparing policy terms and conditions</li>
      <li>purchasing “Long Term” Life Insurance</li>
    </ul>
    <p class="callout" style="margin-top:16px">If you want to ensure that you have someone assisting you if a claim is ever needed to be made.</p>
  </div>

  <svg style="position:absolute;left:0;top:398px" width="295" height="16" viewBox="0 0 295 16">
    <path d="M0 4 C100 10 200 0 295 6 L295 16 L0 16Z" fill="var(--navy)"/>
  </svg>
  <div class="footer-url" style="left:112px">www.halvardmensley.com.au</div>
</section>

<section class="page page--tpd">
  <div class="photo" style="top:0;height:414px;background:linear-gradient(160deg,#4a6a98 0%,#2d4d80 40%,#1c3a6b 75%,#12264a 100%)" role="img" aria-label="Photo of a person in a wheelchair by a bright window, tinted navy"></div>
  <div style="position:absolute;left:6px;top:104px;width:281px;height:246px;background:rgba(230,234,240,.82)"></div>
  <div class="tab" style="right:0">CHEAT SHEET</div>
  <svg style="position:absolute;left:0;top:64px" width="293" height="40" viewBox="0 0 293 40">
    <path d="M28 0 L293 0 L293 40 L18 40 Z" fill="var(--gold)"/>
  </svg>
  <div class="banner-title" style="left:26px;width:267px;top:69px;text-align:center;color:var(--navy);font-size:10.5px">Buying Total and Permanent<br>Disability (TPD) Insurance</div>

  <div class="col" style="left:12px;top:108px;width:132px">
    <h2 class="h-section">How much do I need?</h2>
    <table class="need-table">
      <tr><th>NEED</th><th>AMOUNT</th></tr>
      <tr><td>Repaying Debts</td><td>$</td></tr>
      <tr><td>Medical Expenses</td><td>$</td></tr>
      <tr><td>Home Modification Costs</td><td>$</td></tr>
      <tr><td>Other</td><td>$</td></tr>
      <tr class="total"><td>TOTAL</td><td>$</td></tr>
    </table>
    <h2 class="h-section" style="margin-top:6px">Tips &amp; Traps</h2>
    <div class="tips">
      <p><b>Purchase an “Own Occupation” definition Policy</b> to ensure that you are not tested against your ability to work in “Any Occupation” at claim time.</p>
      <p><b>Review what the policy doesn’t cover “Exclusions”.</b> Standard exclusions for most policies is self-inflicted acts.</p>
      <p>Look to <b>purchase “Long Term” Life Insurance</b> if you think you will need to hold the policy for a number of years. This may save you tens of thousands of dollars over the life of your policy.</p>
      <p>Ensure the contract is <b>guaranteed to be renewed</b> if you pay your premiums until expiry age.</p>
      <p>If purchased through Super, <b>you may be liable for a tax bill</b> in the event of a claim</p>
    </div>
  </div>

  <div class="col" style="left:156px;top:108px;width:130px">
    <h2 class="h-section">Who offers it?</h2>
    <ul class="list">
      <li>Most Superannuation Funds</li>
      <li>Some Private Health Funds</li>
      <li>Some Employers</li>
      <li>Life Insurance Companies</li>
      <li>General Insurance Companies</li>
    </ul>
    <h2 class="h-section" style="margin-top:8px">When to call a professional adviser?</h2>
    <p class="help">If you need help:</p>
    <ul class="list">
      <li>comparing premiums or policies</li>
      <li>reviewing wording of insurance contracts</li>
      <li>matching a policy to suit your occupation</li>
      <li>purchasing “Long Term” Life Insurance</li>
    </ul>
    <p class="callout">If you want to ensure that you have someone assisting your family if a claim is ever needed to be made.</p>
  </div>

  <p class="disclaimer">The information provided on this sheet is general advice only and does not consider your objectives, financial situation and needs. Before acting on it, consider its suitability and seek professional advice.</p>
  <div class="contact">Suite 4, 118 Harbour Road, Kellaway<br>✉ hello@halvardmensley.com.au<br>⊕ www.halvardmensley.com.au</div>
  <div class="legal">Corporate Authorised Representative of Northgate Advisory Partners AFSL 400000</div>
</section>

</body>
</html>
```